Moms Beyond Gnats

My company name is Moms beyond gnats. We do residential and commercial mosquito control. See attached brochure and logo.

Target Market(s)

My target market is upper middle class families in the midwestern part of the US.

Requirements
Must have
• Form to collect customer information

```html
<!DOCTYPE html>
<html lang="en">
<head>
<meta charset="utf-8">
<title>Moms Beyond Gnats — Mosquito Control</title>
<link href="https://fonts.googleapis.com/css2?family=Yanone+Kaffeesatz:wght@400;500;700&family=Arimo:wght@400;700&family=Alfa+Slab+One&display=swap" rel="stylesheet">
<style>
:root{
  --green-dark:#0b5a12;
  --green:#148a1c;
  --green-mid:#1c7a24;
  --green-text:#156b1d;
  --yellow:#fff200;
  --yellow-btn:#f2cd1f;
  --sky-top:#cfe3f5;
  --sky-mid:#7fb2e0;
  --text:#222;
  --text-soft:#444;
  --white:#fff;
}
*{margin:0;padding:0;box-sizing:border-box}
html,body{width:1200px;height:1050px;overflow:hidden}
body{
  position:relative;font-family:"Arimo",Arial,sans-serif;color:var(--text);
  background:linear-gradient(180deg,#fff 60px,#e8f1fa 140px,var(--sky-mid) 330px,#a9cdee 520px,#e3eef8 700px,#f3f7f2 860px,#fff 960px);
}
.site-header{position:absolute;left:0;top:0;width:1200px;height:58px;
  background:linear-gradient(180deg,#1c9a22,#0d6e14);border-bottom:2px solid #a8cde8}
.header-phone{position:absolute;left:135px;top:4px;font-family:"Yanone Kaffeesatz",sans-serif;
  font-weight:700;font-size:44px;color:var(--white);line-height:48px}
.main-nav{position:absolute;left:499px;top:21px;display:flex;gap:0}
.main-nav a{color:var(--white);text-decoration:none;font-weight:700;font-size:14px;margin-right:0}
.main-nav a:nth-child(1){margin-right:60px}
.main-nav a:nth-child(2){margin-right:63px}
.main-nav a:nth-child(3){margin-right:60px}
.main-nav a:nth-child(4){margin-right:56px}
.brand{position:absolute;left:128px;top:68px;width:230px;height:142px;background:var(--white);
  display:flex;align-items:center;justify-content:center;gap:10px}
.brand-mark{width:18px;height:18px;background:var(--green-text)}
.brand-name{font-family:"Arimo",sans-serif;font-weight:700;font-size:22px;color:var(--green-text);line-height:1.1;width:150px}
.hero-title{position:absolute;left:97px;top:236px;width:345px;font-family:"Yanone Kaffeesatz",sans-serif;
  font-weight:400;font-size:46px;line-height:48px;color:var(--white);text-shadow:1px 2px 3px rgba(0,0,0,.45)}
.hero-photo{position:absolute;left:440px;top:58px;width:677px;height:368px;
  background:linear-gradient(160deg,#b9c9a8 0%,#8fa86c 35%,#d8dde4 62%,#a6b7cc 100%)}
.hero-band{position:absolute;left:424px;top:398px;width:694px;height:34px}
.hero-band svg{position:absolute;inset:0}
.hero-band p{position:relative;padding:6px 0 0 12px;font-family:"Yanone Kaffeesatz",sans-serif;
  font-weight:700;font-size:23px;color:var(--green-text)}
.info-cols{position:absolute;left:89px;top:426px;width:1028px;height:202px;display:flex}
.info-col{flex:1;background:rgba(215,232,248,.55);border-right:1px solid rgba(255,255,255,.7);padding:22px 14px 0 36px}
.info-col:nth-child(2){padding-left:16px}
.info-col:nth-child(3){padding-left:22px;border-right:0}
.info-col h2{font-family:"Alfa Slab One",serif;font-weight:400;font-size:28px;line-height:28px;color:var(--green);letter-spacing:1px}
.info-col h3{font-size:13px;font-weight:700;color:#1e2a36;margin:6px 0 8px}
.info-col p{font-size:14px;line-height:20px;color:var(--text-soft)}
.request{position:absolute;left:89px;top:607px;width:357px;height:350px}
.request svg{position:absolute;inset:0}
.request-title{position:absolute;left:23px;top:3px;font-family:"Yanone Kaffeesatz",sans-serif;font-weight:700;font-size:25px;color:var(--green-dark)}
.request-form{position:absolute;left:22px;top:25px;width:330px;height:323px;background:var(--green-dark);border-radius:10px 6px 0 12px;padding:22px 16px 0 0}
.field{display:flex;align-items:center;justify-content:flex-end;margin-bottom:18px}
.field label{color:var(--white);font-size:14px;margin-right:8px}
.field input{width:243px;height:27px;border:1px solid #cfd;background:var(--white)}
.field:nth-child(4){margin-bottom:24px}
.form-question{color:#e8f2e8;font-size:14px;margin-left:15px}
.choices{display:flex;gap:16px;margin:12px 0 0 20px;color:var(--white);font-size:14px}
.choices span{display:flex;align-items:center;gap:9px}
.choices i{width:14px;height:14px;background:#ddd;display:inline-block}
.submit{position:absolute;right:14px;bottom:24px;width:128px;height:49px;border:1px solid #d8b51a;border-radius:5px;
  background:linear-gradient(180deg,#fff3a0,var(--yellow-btn) 60%,#e0b316);font-family:"Arimo",sans-serif;font-weight:700;font-size:20px;color:#5a4a08;letter-spacing:.5px}
.eco{position:absolute;left:492px;top:645px;width:620px}
.eco h2{font-weight:400;font-size:24px;color:#1b3d26}
.eco h2 em{color:var(--green-text)}
.eco-copy{position:absolute;left:492px;top:693px;width:320px;font-size:16px;line-height:22px;color:#111}
.eco-cta{position:absolute;left:492px;top:807px;width:320px;font-size:16px;line-height:24px;font-weight:700;color:#111}
.eco-phone{position:absolute;left:497px;top:884px;font-family:"Yanone Kaffeesatz",sans-serif;font-weight:700;font-size:52px;color:var(--green-text);line-height:60px}
.eco-badge{position:absolute;left:870px;top:694px}
.footer-shadow{position:absolute;left:40px;top:990px;width:1120px;height:14px;
  background:radial-gradient(ellipse at center top,rgba(0,0,0,.12),transparent 70%)}
.copyright{position:absolute;left:0;top:1016px;width:1212px;text-align:center;font-size:12px;font-weight:700;color:#666}
</style>
</head>
<body>
<header class="site-header">
  <div class="header-phone">CALL (555) 014-2290</div>
  <nav class="main-nav"><a href="#">HOME</a><a href="#">ABOUT</a><a href="#">PRODUCTS</a><a href="#">SERVICES</a><a href="#">CONTACT</a></nav>
</header>

<div class="brand"><span class="brand-mark"></span><span class="brand-name">Moms Beyond Gnats</span></div>

<h1 class="hero-title">Rid your outside areas of pesky and dangerous bugs the safe way!</h1>

<div class="hero-photo" role="img" aria-label="Family enjoying a barbecue lunch at a garden table"></div>

<div class="hero-band">
  <svg width="694" height="34" viewBox="0 0 694 34"><polygon points="0,0 694,16 694,20 8,34" fill="#fff200"/><polygon points="0,0 694,0 694,20 8,34" fill="#fff200"/></svg>
  <p>Once applied, M.B.G! is a long acting product that remains effective for weeks.</p>
</div>

<section class="info-cols">
  <article class="info-col"><h2>WHAT</h2><h3>IS MOMS BEYOND GNATS?</h3>
    <p>Moms Beyond Gnats is the only scheduled spraying service devoted exclusively to protecting your outdoor area against mosquitoes and other pests all season long!</p></article>
  <article class="info-col"><h2>WHY</h2><h3>USE MOMS BEYOND GNATS?</h3>
    <p>West Nile Virus is a real threat! Illinois is one of the states with the most confirmed human cases. M.B.G! will protect your business against West Nile and eliminate or reduce the dangers of Encephalitis and allergic reactions caused by insect bites.</p></article>
  <article class="info-col"><h2>WHERE</h2><h3>CAN I SPRAY MOMS BEYOND GNATS?</h3>
    <p>Anywhere outside. M.B.G! offers excellent service for public pools, outdoor cafés and beer gardens, baseball fields, courtyards, public places such as fountains or town squares, and office gathering areas.</p></article>
</section>

<section class="request">
  <svg width="357" height="350" viewBox="0 0 357 350"><polygon points="0,0 357,18 352,350 22,350" fill="#fff200"/></svg>
  <div class="request-title">REQUEST INFORMATION</div>
  <form class="request-form">
    <div class="field"><label>Name</label><input type="text"></div>
    <div class="field"><label>Email</label><input type="text"></div>
    <div class="field"><label>Phone</label><input type="text"></div>
    <div class="field"><label>Address</label><input type="text"></div>
    <p class="form-question">I would like to schedule an evaluation?</p>
    <div class="choices"><span><i></i>yes</span><span><i></i>not yet</span></div>
    <button class="submit" type="button">SUBMIT</button>
  </form>
</section>

<div class="eco"><h2>Environmentally-friendly <em>EPA-APPROVED</em> treatment</h2></div>
<p class="eco-copy">Keep your customers and employees enjoying the summer weather without the inconvenience of mosquitoes, ticks, lice and other insects.</p>
<p class="eco-cta">Call (555) 014-2290 to schedule an evaluation appointment or feel out the form to the right.</p>
<div class="eco-phone">CALL (555) 014-2290</div>
<svg class="eco-badge" width="140" height="140" viewBox="0 0 140 140" aria-hidden="true">
  <circle cx="70" cy="70" r="66" fill="none" stroke="#1f9a3a" stroke-width="5"/>
  <circle cx="70" cy="70" r="50" fill="none" stroke="#1f9a3a" stroke-width="3"/>
</svg>

<div class="footer-shadow"></div>
<p class="copyright">Copyright 2010 Moms Beyond Gnats! All Rights Reserved</p>
</body>
</html>
```